I need a design for Brightmoor Homes which is a custom home builder. The name on it will be Dan Porter, and I will give the phone number to the winning design. No address or website needed.

```html
<!DOCTYPE html>
<html lang="en">
<head>
<meta charset="utf-8">
<title>Brightmoor Homes – Business Card</title>
<link rel="stylesheet" href="https://fonts.googleapis.com/css2?family=Open+Sans:wght@400&display=swap">
<style>
  :root {
    --page: #ffffff;
    --card: #000000;
    --brand-grey: #bcbec0;
    --accent-red: #ed1c24;
    --text-white: #ffffff;
  }
  * { margin: 0; padding: 0; box-sizing: border-box; }
  html, body {
    width: 1200px;
    height: 702px;
    overflow: hidden;
    background: var(--page);
  }
  .canvas {
    position: relative;
    width: 1200px;
    height: 702px;
    background: var(--page);
  }
  .card {
    position: absolute;
    left: 58px;
    top: 58px;
    width: 1068px;
    height: 612px;
    background: var(--card);
    font-family: "Open Sans", "Helvetica Neue", Arial, sans-serif;
  }
  .brand {
    position: absolute;
    left: 46px;
    top: 118px;
    display: flex;
    align-items: center;
    gap: 26px;
  }
  .brand-name {
    color: var(--brand-grey);
    font-size: 104px;
    font-weight: 400;
    line-height: 1;
    letter-spacing: -2px;
    white-space: nowrap;
  }
  .brand-mark {
    width: 34px;
    height: 34px;
    background: var(--accent-red);
    flex: none;
  }
  .contact {
    position: absolute;
    left: 66px;
    top: 386px;
    color: var(--text-white);
    font-weight: 400;
    font-size: 56px;
    line-height: 1.7;
  }
</style>
</head>
<body>
  <div class="canvas">
    <section class="card">
      <div class="brand">
        <span class="brand-name">Brightmoor Homes</span>
        <span class="brand-mark" aria-hidden="true"></span>
      </div>
      <div class="contact">
        <p class="contact-name">Dan Porter</p>
        <p class="contact-phone">555.014.2290</p>
      </div>
    </section>
  </div>
</body>
</html>
```